Rising Stewards Scheme. Brochure to Inform Target Audience.

Rising Steward Scheme:

4 Page Brochure
Aimed at Parents and Children (Age 11-16)
Programme Overview
Specific Focus on Copperleaf Award with Learning Objectives and Enabling Objectives from Content Document
Contact Area Needed
How to Book - Online through the Website
Should encourage people to want to join it or sign up

you can use stock rugby images if needed

Target Market(s)

children between ages 11-16 and parents, gatekeepers (schools, rugby clubs)

Industry/Entity Type

Education

Font styles to use
Serif
Sans Serif

Requirements
Must have
• the programme content, each award continent and Copperleaf Award learning objectives
• Colours should match existing work that has been created
• Get in touch: www.harvestmark-rss.com
• maren@harvestmark-rss.com
Nice to have
• graphics of kids playing rugby if possible from stock images

```html
<!DOCTYPE html>
<html lang="en">
<head>
<meta charset="utf-8">
<title>Rising Stewards Scheme – Brochure Spread</title>
<link rel="stylesheet" href="https://fonts.googleapis.com/css2?family=Montserrat:wght@400;600;700;800&family=Open+Sans:ital,wght@0,400;0,700;1,700&display=swap">
<style>
  :root {
    --gold: #f6b90f;
    --gold-soft: #fdd34a;
    --ink: #1b1b1b;
    --panel: rgba(8, 8, 8, 0.9);
    --tab: #3a3a3a;
    --white: #ffffff;
    --paper: #f4f2ec;
    --body: #2a2a2a;
  }
  html, body { margin: 0; padding: 0; overflow: hidden; background: #ffffff; }
  .spread {
    position: relative;
    width: 1200px;
    height: 849px;
    overflow: hidden;
    font-family: "Open Sans", Arial, sans-serif;
  }

  /* ---------- back page ---------- */
  .back-page { position: absolute; left: 0; top: 0; width: 600px; height: 849px; }
  .field-photo {
    position: absolute; left: 0; top: 0; width: 600px; height: 560px;
    background: linear-gradient(180deg, #1f2a1c 0%, #34502a 45%, #6f8f3a 80%, #9db556 100%);
  }
  .faq-panel {
    position: absolute; left: 45px; top: 38px; width: 486px; height: 445px;
    background: var(--panel);
    box-sizing: border-box; padding: 14px 22px 0 26px;
    color: var(--white);
  }
  .faq-title {
    margin: 0 0 12px; font-family: "Montserrat", Arial, sans-serif;
    font-weight: 800; font-size: 40px; line-height: 1; color: var(--gold);
  }
  .faq-item { margin: 0 0 9px; font-size: 8.9px; line-height: 1.32; }
  .faq-q { display: block; color: var(--gold); font-weight: 700; }
  .faq-a { display: block; color: var(--white); }

  .mission-band {
    position: absolute; left: 0; top: 535px; width: 600px; height: 75px;
    background: var(--paper);
  }
  .section-tab {
    position: absolute; left: 42px; height: 32px; padding: 0 30px 0 14px;
    background: var(--tab); color: var(--gold-soft);
    font-family: "Montserrat", Arial, sans-serif; font-weight: 700; font-size: 20px;
    line-height: 32px;
    clip-path: polygon(0 0, 100% 0, 88% 100%, 0 100%);
  }
  .mission-tab { top: 542px; }
  .mission-text {
    position: absolute; left: 55px; top: 585px; margin: 0;
    font-family: "Montserrat", Arial, sans-serif; font-weight: 700; font-size: 9.6px;
    color: var(--ink);
  }

  .about-block {
    position: absolute; left: 0; top: 610px; width: 600px; height: 239px;
    background: var(--gold);
  }
  .about-tab { top: 620px; color: var(--white); }
  .about-text {
    position: absolute; left: 55px; top: 662px; width: 500px;
    font-size: 9.4px; line-height: 1.42; color: var(--body);
  }
  .about-text p { margin: 0 0 9px; }
  .about-text .learn-more { font-weight: 700; font-style: italic; }

  /* ---------- cover page ---------- */
  .cover-page { position: absolute; left: 600px; top: 0; width: 600px; height: 849px; }
  .match-photo {
    position: absolute; inset: 0;
    background: linear-gradient(180deg, #1e2a18 0%, #3f6a2b 40%, #6e9a3d 75%, #a4c25c 100%);
  }
  .cover-accent { position: absolute; left: 0; top: 0; width: 600px; height: 849px; }

  .brand {
    position: absolute; left: 48px; top: 40px; width: 190px; text-align: center;
    font-family: "Montserrat", Arial, sans-serif; font-weight: 700; color: var(--gold);
  }
  .brand-mark {
    width: 56px; height: 56px; margin: 0 auto 8px;
    border: 3px solid var(--gold); border-radius: 50%; box-sizing: border-box;
  }
  .brand-name { font-size: 10px; letter-spacing: 1px; line-height: 1.2; margin-bottom: 10px; }
  .brand-scheme { font-size: 15px; letter-spacing: 0.5px; line-height: 1.2; }

  .headline {
    position: absolute; left: 258px; top: 52px; margin: 0;
    font-family: "Montserrat", Arial, sans-serif; font-weight: 400;
    font-size: 31px; line-height: 1.12; color: var(--white); letter-spacing: 0.5px;
  }
  .headline strong { display: block; font-weight: 800; color: var(--gold); }
</style>
</head>
<body>
<div class="spread">

  <section class="back-page">
    <div class="field-photo" role="img" aria-label="Rugby ball resting on a dark, blurred grass pitch"></div>

    <div class="faq-panel">
      <h2 class="faq-title">FAQ</h2>
      <p class="faq-item"><span class="faq-q">Will you provide lunch or snacks?</span><span class="faq-a">Water will be provided to refill water bottles. However, we ask that children bring their own lunch.</span></p>
      <p class="faq-item"><span class="faq-q">Who attends your Rising Stewards Scheme?</span><span class="faq-a">Children of all abilities, some who have played rugby before and some who have never played. The programme is available to both boys and girls.</span></p>
      <p class="faq-item"><span class="faq-q">When do I drop and pick up my child from the programme?</span><span class="faq-a">Venue timings are included in your welcome letter. Typically the drop off time is 0900 and collection time at 1600. Please ensure your child is handed over and registered to one of our coaches on the programme before you leave.</span></p>
      <p class="faq-item"><span class="faq-q">What should my child wear?</span><span class="faq-a">Activities will take place both indoor and outdoor; therefore, please ensure you bring appropriate rugby kit, including waterproofs and a change of kit, also trainers and boots.</span></p>
      <p class="faq-item"><span class="faq-q">What makes your programme the right choice for my child?</span><span class="faq-a">The programme is fun and designed to develop the child's leadership skills on and off the pitch. These skills will help them grow as individuals.</span></p>
      <p class="faq-item"><span class="faq-q">How can I enrol on the silver or gold award?</span><span class="faq-a">In order to enrol on the Silver Award the child must have successfully completed the Copperleaf Award. In order to enrol on the Gold Award the child must have successfully completed the Silver Award.</span></p>
      <p class="faq-item"><span class="faq-q">Will I meet a Guardian?</span><span class="faq-a">Yes. Whilst on the programme you will have a chance to meet and learn from a Guardian.</span></p>
      <p class="faq-item"><span class="faq-q">How do you comply with safeguarding?</span><span class="faq-a">This is really important to us. We want all children to experience a fun, healthy and safe environment; therefore, our coaches and staff are educated and trained in safeguarding, child protection and are all DBS checked.</span></p>
    </div>

    <div class="mission-band"></div>
    <div class="section-tab mission-tab">Our Mission</div>
    <p class="mission-text">TO EDUCATE, INSPIRE, MENTOR AND TRANSFER KEY LEADERSHIP SKILLS TO THE NEXT GENERATION</p>

    <div class="about-block"></div>
    <div class="section-tab about-tab">Guardians</div>
    <div class="about-text">
      <p>Ironvale Guardians, a world first is the fulfilment of a desire to create a colossal force for good; it emanates from the recognition and unification of rugby's finest warriors. This is a kinship of iconic men and women who have represented their countries in 100 international rugby test matches.</p>
      <p>Only three in every 1000 international rugby players ever reach this massive milestone. As members of Ironvale Guardians the Toughest Membership in the World, this rare and select breed of rugby players are uplifting lives by making the wonderful game more accessible and desirable to the growing number of rugby fans and players across the globe. Ironvale Guardians are luminaries, gladiators and warriors. But above all they are people. They have given so much. And now, as a unified force, they're giving back even more.</p>
      <p>Ironvale Guardians are luminaries, gladiators and warriors. But above all they are people. They have given so much. And now, as a unified force, they're giving back even more.</p>
      <p class="learn-more">Learn More: www.ironvaleguardians.com</p>
    </div>
  </section>

  <section class="cover-page">
    <div class="match-photo" role="img" aria-label="Two young rugby players in a tackle on a grass pitch, one in a red shirt and one in blue and white holding the ball"></div>
    <svg class="cover-accent" viewBox="0 0 600 849" aria-hidden="true">
      <polygon points="250,849 600,600 600,849" fill="#f6b90f" opacity="0.45"/>
      <polygon points="330,849 600,650 600,849" fill="#f6b90f"/>
    </svg>

    <div class="brand">
      <div class="brand-mark"></div>
      <div class="brand-name">IRONVALE GUARDIANS</div>
      <div class="brand-scheme">RISING STEWARDS SCHEME</div>
    </div>

    <h1 class="headline">LEARN TO LEAD<br>AND PLAY THE<strong>GUARDIANS WAY</strong></h1>
  </section>

</div>
</body>
</html>
```